Plakate für TQ Car Wash
Zielgruppe
TQ Car Wash
SB Waschpark mit 4 Plätzen
Zielgruppe: Alle Autofahrer aus der Region
Marketing wg. Neueröffnung
Aufgabenstellung
Design ist für zwei Planen an einem Werbeanhänger
2200mm x 4750mm Fläche
Aussagen, Logo (kann ähnlich sein oder als eps bzw ai geliefert werden) als Ideenskizze in den Dateien mitgeliwfert. Open to new ideas.

```html
<!DOCTYPE html>
<html lang="de">
<head>
<meta charset="utf-8">
<title>TQ Car Wash – Neueröffnung</title>
<link href="https://fonts.googleapis.com/css2?family=Montserrat:wght@700;800&family=Arimo:wght@700&display=swap" rel="stylesheet">
<style>
  :root {
    --navy: #163a66;
    --sky: #2aa3e0;
    --orange: #f4a40a;
    --white: #ffffff;
    --mist-light: #eef1f6;
    --mist-mid: #c9d2e1;
    --photo-red: #b8283a;
    --photo-steel: #8e9bb0;
    --shirt-grey: #4a5058;
  }
  * { margin: 0; padding: 0; box-sizing: border-box; }
  html, body { width: 1200px; height: 556px; overflow: hidden; background: var(--white); }
  .banner {
    position: relative;
    width: 1200px;
    height: 556px;
    overflow: hidden;
    background: radial-gradient(ellipse at 75% 45%, var(--mist-light) 0%, #dde3ee 55%, var(--mist-mid) 100%);
    font-family: "Montserrat", sans-serif;
  }
  .wash-photo {
    position: absolute;
    left: 0; top: 0;
    width: 640px; height: 505px;
    background:
      radial-gradient(ellipse 40% 30% at 22% 72%, rgba(230,120,60,0.55) 0%, transparent 100%),
      linear-gradient(175deg, #4f5f7c 0%, #a9b4c6 30%, var(--photo-red) 55%, #9a2233 78%, #d9dde4 100%);
    -webkit-mask-image: linear-gradient(90deg, #000 65%, transparent 100%);
            mask-image: linear-gradient(90deg, #000 65%, transparent 100%);
  }
  .model-photo {
    position: absolute;
    left: 260px; top: 30px;
    width: 470px; height: 475px;
    background: linear-gradient(180deg,
      #3a2e2a 0%, #9c7565 14%, #b9907c 30%, #8a6a5c 44%,
      #555b64 52%, var(--shirt-grey) 70%, #3f454d 100%);
    -webkit-mask-image: radial-gradient(ellipse 52% 78% at 50% 78%, #000 72%, transparent 100%);
            mask-image: radial-gradient(ellipse 52% 78% at 50% 78%, #000 72%, transparent 100%);
    opacity: 0.92;
  }
  .opening-badge {
    position: absolute;
    left: 92px; top: 30px;
    width: 242px; height: 242px;
    border-radius: 50%;
    background: var(--orange);
    border: 6px solid var(--white);
    color: var(--white);
    display: flex;
    flex-direction: column;
    align-items: center;
    justify-content: center;
    transform: rotate(-5deg);
    text-align: center;
  }
  .opening-badge .badge-word { font-size: 40px; font-weight: 800; line-height: 1.05; }
  .opening-badge .badge-date { font-size: 23px; font-weight: 700; margin-top: 8px; }
  .headline {
    position: absolute;
    left: 640px; top: 32px;
    width: 430px;
    text-align: center;
    color: var(--navy);
    font-weight: 800;
    font-size: 76px;
    line-height: 80px;
    letter-spacing: 1px;
  }
  .brand {
    position: absolute;
    left: 838px; top: 424px;
    display: flex;
    align-items: center;
    gap: 12px;
    color: var(--navy);
    font-weight: 800;
    font-size: 40px;
    line-height: 1;
    white-space: nowrap;
  }
  .brand .brand-dot {
    width: 22px; height: 22px;
    border-radius: 50%;
    background: var(--sky);
  }
  .location-bar {
    position: absolute;
    left: 0; top: 505px;
    width: 1200px; height: 51px;
    background: var(--navy);
    color: var(--white);
    font-family: "Arimo", sans-serif;
    font-weight: 700;
    font-size: 25px;
    line-height: 51px;
    padding-left: 27px;
  }
</style>
</head>
<body>
  <main class="banner">
    <div class="wash-photo" role="img" aria-label="Foto: eingeschäumtes Autoheck mit rotem Rücklicht"></div>
    <div class="model-photo" role="img" aria-label="Foto: lächelnder Mann im grauen T-Shirt mit erhobenem Daumen"></div>

    <div class="opening-badge">
      <span class="badge-word">Neu-</span>
      <span class="badge-word">eröffnung</span>
      <span class="badge-date">ab xx.xx.</span>
    </div>

    <h1 class="headline">EINFACH.<br>BESSER.<br>SAUBER.</h1>

    <div class="brand">
      <span class="brand-dot"></span>
      <span class="brand-name">TQ Car Wash</span>
    </div>

    <footer class="location-bar">In Birkenmoor hinter der Feuerwehr</footer>
  </main>
</body>
</html>
```